Stationery for use with Ninefold Ridge reports

I would like to get a stationery design that my firm -- Ninefold Ridge Advisory -- will use as a format for reports that we send our clients. I am specifically looking for a design for use on a piece of paper or letterhead -- not business cards or envelopes.

We are an Africa based US risk intelligence and strategy firm that works with multinational corporations operating in West Africa. Our initial thinking is that we would like a color scheme consistent with our existing logo -- however we are open to other color schemes.

Also, we would like to see at least two separate versions: one with our company name and logo, the other without name and logo.

We also would like font recommendations for the stationary design.

The final design should communicate discreet professionalism and a modern approach, but it should not overshadow the words and information printed on the stationery.

Target Market(s)

Multinational corporations that currently use our products.

Font styles to use
Serif
Sans Serif

Requirements
Must have
• Sense of discreet professionalism that will not overshadow the content we put onto the stationery format.
• We would like to see designs with and without our company name/logo.
• Please suggest fonts that would work with the stationery.
Nice to have
• Ideally colors consistent with out existing logo, though we are open to and even encourage other ideas.
Should not have
• No need for business cards or envelopes.

```html
<!DOCTYPE html>
<html lang="en">
<head>
<meta charset="utf-8">
<title>Ninefold Ridge Advisory — Letterhead</title>
<link rel="stylesheet" href="https://fonts.googleapis.com/css2?family=Arimo:wght@400;700&display=swap">
<style>
  :root {
    --backdrop: #e4e4e4;
    --paper: #ffffff;
    --brand-navy: #22394a;
    --text-body: #4a4a4a;
    --text-greeting: #4f4f4f;
    --signature-tone: #ececec;
  }
  * { margin: 0; padding: 0; box-sizing: border-box; }
  html, body {
    width: 1200px; height: 1141px; overflow: hidden;
    background: var(--backdrop);
    font-family: "Arimo", Arial, sans-serif;
  }
  .letterhead {
    position: absolute; left: 210px; top: 23px;
    width: 780px; height: 1095px;
    background: var(--paper);
    color: var(--text-body);
  }
  .brand-name {
    position: absolute; top: 96px; left: 0; width: 100%;
    text-align: center;
    color: var(--brand-navy);
    font-weight: 700; font-size: 30px; line-height: 34px;
    letter-spacing: 0.5px;
  }
  .greeting {
    position: absolute; left: 58px; top: 274px;
    font-size: 18.5px; color: var(--text-greeting);
  }
  .letter-body {
    position: absolute; left: 58px; top: 331px; width: 664px;
    font-size: 11px; line-height: 16.5px; text-align: justify;
  }
  .letter-body p { margin-bottom: 16.5px; }
  .closing {
    position: absolute; left: 58px; top: 697px; font-size: 11px;
  }
  .signature-area {
    position: absolute; left: 52px; top: 734px;
    width: 226px; height: 66px;
    background: linear-gradient(90deg, var(--signature-tone), #f7f7f7);
    border-radius: 4px;
  }
  .contact-footer {
    position: absolute; left: 58px; right: 58px; top: 1040px;
    font-size: 11.5px; line-height: 15px; color: var(--text-body);
  }
  .contact-block { position: absolute; top: 0; }
  .contact-address { left: 0; }
  .contact-phones { left: 274px; }
  .contact-online { left: 488px; }
  .contact-line { display: flex; align-items: center; gap: 7px; }
  .contact-line svg { width: 10px; height: 10px; fill: var(--brand-navy); flex: none; }
</style>
</head>
<body>
  <main class="letterhead">
    <div class="brand-name">Ninefold Ridge Advisory</div>

    <p class="greeting">Dear Mr. Smith,</p>

    <section class="letter-body">
      <p>Lorem ipsum dolor sit amet, consectetur adipiscing elit. Donec orci purus, luctus vitae dignissim eu, iaculis sed purus. Vivamus faucibus, ipsum nec aliquet viverra, leo mauris condimentum ligula, sit amet sagittis enim ligula quis arcu. Nam egestas tortor id nisi porttitor mattis. In tortor ante, ultricies in suscipit a, tempus non massa. Vivamus et auctor mi. Fusce vel massa nulla. Phasellus nec eros mauris, et scelerisque orci.</p>
      <p>Donec malesuada orci vitae nulla accumsan porta a id massa. Quisque accumsan iaculis magna sit amet fringilla. Maecenas consequat, magna eget tincidunt semper, odio nibh rutrum mi, id feugiat ante nisi eu risus. Vestibulum nunc orci, rhoncus a placerat in, ultricies in mi. Cras mattis varius eros, vel fringilla nisi suscipit eget. Quisque scelerisque sagittis nulla at porttitor.</p>
      <p>Sed id augue vitae urna euismod commodo aliquet a quam. Pellentesque arcu velit, cursus et malesuada ut, consequat et diam. Nullam erat sem, rhoncus id ullamcorper vitae, rhoncus et arcu. In ultricies ultricies nulla, ut rutrum nisi iaculis at. Donec eu magna a metus ornare faucibus. Fusce aliquet faucibus ultricies. Morbi semper, est id tincidunt gravida, sem arcu adipiscing lacus, ac bibendum nulla leo eu purus. Quisque nec diam sed risus consectetur a ccumsan quis quis nibh. Vestibulum id purus lorem.</p>
      <p>It is a long established fact that a reader will be distracted by the readable content of a page when looking at its layout. The point of using Lorem Ipsum is that it has a more-or-less normal distribution of letters, as opposed to using 'Content here, content here', making it look like readable English. Many desktop publishing packages</p>
      <p>ada ut, consequat et diam. Nullam erat sem, rhoncus id ullamcorper vitae, rhoncus et arcu. In ultricies ultricies nulla, ut rutrum nisi iaculis at. Donec eu magna a metus ornare faucibus. Fusce aliquet faucibus ultricies. Morbi semper,</p>
    </section>

    <p class="closing">Sincerely,</p>
    <div class="signature-area" role="img" aria-label="Handwritten signature of Claire Odaro"></div>

    <footer class="contact-footer">
      <div class="contact-block contact-address">
        <div>218 Harbor Crest Road</div>
        <div>Juneau, Alaska 99801</div>
      </div>
      <div class="contact-block contact-phones">
        <div class="contact-line">
          <svg viewBox="0 0 10 10"><path d="M2 0.5 L3.6 2.6 L2.7 3.6 Q3.8 5.8 6.3 7.2 L7.4 6.3 L9.5 7.9 L8.4 9.5 Q2.5 8.6 0.5 1.6 Z"/></svg>
          <span>555-014-2290</span>
        </div>
        <div class="contact-line">
          <svg viewBox="0 0 10 10"><rect x="2.5" y="0.5" width="5" height="3"/><rect x="0.5" y="3.5" width="9" height="4" rx="0.8"/><rect x="2.5" y="7" width="5" height="2.5"/></svg>
          <span>555-018-7734</span>
        </div>
      </div>
      <div class="contact-block contact-online">
        <div class="contact-line">
          <svg viewBox="0 0 10 10"><path d="M0.5 2 H9.5 V8.5 H0.5 Z M0.5 2 L5 5.5 L9.5 2" stroke="#fff" stroke-width="0.8"/></svg>
          <span>info@ninefoldridge.com</span>
        </div>
        <div class="contact-line">
          <svg viewBox="0 0 10 10"><circle cx="5" cy="5" r="4.5"/></svg>
          <span>www.ninefoldridge.com</span>
        </div>
      </div>
    </footer>
  </main>
</body>
</html>
```